キャリア層をターゲットとしたセミナーを開催予定です。落ち着いた雰囲気のデザインをお願いします。(講演内容は添付ファイルをご確認ください)
開催団体:一般社団法人あおぞら地域交流センター
〒521-0342滋賀県米原市柏原台4-7-15
TEL:0749-38-2951
TEL:0120-394-667
A4
片面
• 高解像度JPG (.jpg)

洗練されたデザインや文字の配置、対象となるターゲットにフィットすると思い選択いたしました。
ご提案ありがとうございました。

皆さま、貴重なアイディアをくださり本当にありがとうございました。
どれか一つ選択することが大変心苦しいのですが、
今回このような結果を出させていただきました。
今後ともよろしくお願いいたします。

```html
<!DOCTYPE html>
<html lang="ja">
<head>
<meta charset="utf-8">
<title>言葉が人を動かす、自分を変える｜オンライン講座</title>
<link href="https://fonts.googleapis.com/css2?family=Shippori+Mincho:wght@500;700;800&family=Noto+Sans+JP:wght@400;500;700;900&display=swap" rel="stylesheet">
<style>
:root{
  --cream:#f3eee3;
  --paper:#fbf8f1;
  --navy:#1f3350;
  --ink:#2c2f36;
  --orange:#e5843a;
  --orange-soft:#f2c39a;
  --line:#b9ad98;
  --muted:#6b6459;
}
*{margin:0;padding:0;box-sizing:border-box}
html,body{width:849px;height:1200px;overflow:hidden;background:var(--cream)}
body{font-family:"Noto Sans JP",sans-serif;color:var(--ink)}
.flyer{position:relative;width:849px;height:1200px;background:var(--cream)}
.mincho{font-family:"Shippori Mincho",serif}

/* date tag */
.date-tag{position:absolute;left:22px;top:14px;width:116px;height:142px;background:var(--orange);color:#fff;text-align:center;padding-top:12px}
.date-tag .kind{font-size:13px;font-weight:700;letter-spacing:.05em}
.date-tag .year{font-size:13px;margin-top:4px}
.date-tag .day{font-family:"Shippori Mincho",serif;font-size:30px;font-weight:800;line-height:1.05}
.date-tag .day small{font-size:14px}
.date-tag .time{font-size:13px;font-weight:700;margin-top:2px}
.date-tag .note{font-size:9px;margin-top:6px;border-top:1px solid rgba(255,255,255,.6);margin-left:12px;margin-right:12px;padding-top:5px}

/* headline */
.headline{position:absolute;left:340px;top:18px;font-family:"Shippori Mincho",serif;font-weight:800;color:var(--navy);line-height:1.15}
.headline .l1{font-size:54px;letter-spacing:.02em}
.headline .l2{font-size:54px;margin-left:126px;display:block}
.headline em{font-style:normal;color:var(--orange)}

/* mug illustration */
.mug{position:absolute;left:582px;top:160px;width:194px;height:206px}

/* theme card */
.theme-card{position:absolute;left:112px;top:176px;width:440px;height:272px;background:var(--paper);transform:rotate(-3deg);box-shadow:3px 5px 10px rgba(60,45,20,.18)}
.cube{position:absolute;left:48px;top:24px;width:58px;height:56px}
.theme-title{position:absolute;left:110px;top:44px;font-family:"Shippori Mincho",serif;font-weight:800;color:var(--navy);font-size:30px;line-height:1.45}
.theme-title .accent{color:var(--navy);border-bottom:4px solid var(--orange-soft)}
.pencil{position:absolute;left:372px;top:196px;width:70px;height:14px;transform:rotate(-28deg)}

/* details */
.home-study{position:absolute;left:160px;top:418px;font-family:"Shippori Mincho",serif;font-weight:700;font-size:20px;color:var(--navy);transform:rotate(-3deg)}
.details{position:absolute;left:180px;top:456px;width:230px;font-size:12.5px;border-collapse:collapse}
.details th{background:var(--orange);color:#fff;font-weight:500;width:52px;padding:4px 0;text-align:center}
.details td{padding:4px 10px;color:var(--ink);border-bottom:1px solid var(--line)}
.details tr+tr th{border-top:3px solid var(--cream)}

/* curriculum */
.question{position:absolute;left:590px;top:384px;font-family:"Shippori Mincho",serif;font-weight:800;font-size:22px;color:var(--navy);line-height:1.45}
.curriculum{position:absolute;left:590px;top:466px;width:240px}
.curriculum .label{display:flex;align-items:center;gap:8px;font-size:13px;color:var(--navy);font-weight:700}
.curriculum .label span{background:var(--orange);color:#fff;padding:2px 8px;font-weight:500;font-size:12px}
.curriculum ul{list-style:none;margin-top:7px;font-size:11.5px;line-height:1.75}
.curriculum li::before{content:"・";color:var(--orange)}

/* vertical stories */
.stories{position:absolute;left:16px;top:612px;width:820px;height:368px;display:flex;gap:14px;justify-content:space-between}
.story{writing-mode:vertical-rl;height:368px;font-size:12px;line-height:1.9;color:var(--ink);font-family:"Shippori Mincho",serif;font-weight:500}
.story h3{font-family:"Shippori Mincho",serif;font-weight:800;font-size:17px;color:var(--navy);margin-left:10px;line-height:1.5}
.story h3 em{font-style:normal;color:var(--orange)}
.story p{margin-left:6px}
.story .hl{color:var(--orange);font-weight:700}
.story.s-left{width:298px}
.story.s-mid{width:252px;border-left:1px solid var(--line);border-right:1px solid var(--line);padding:0 12px}
.story.s-right{width:240px}

/* footer */
.footer{position:absolute;left:0;top:990px;width:849px;height:150px;border-top:1px solid var(--line)}
.contact{position:absolute;left:32px;top:10px}
.contact .cap{font-size:12px;color:var(--navy);font-weight:700;background:var(--orange);color:#fff;padding:2px 10px;display:inline-block}
.contact .tel{display:flex;align-items:center;gap:8px;margin-top:10px;font-family:"Noto Sans JP",sans-serif;font-weight:900;font-size:34px;color:var(--navy);letter-spacing:.02em}
.contact .tel svg{width:36px;height:24px}
.contact .hours{font-size:11px;color:var(--muted);margin-top:2px}
.search{position:absolute;left:256px;top:12px;display:flex;border:1px solid var(--navy);height:24px;font-size:11px}
.search .word{padding:3px 10px;background:#fff;color:var(--navy);font-weight:700}
.search .btn{width:26px;background:var(--navy);display:flex;align-items:center;justify-content:center}
.organizer{position:absolute;left:440px;top:10px;display:flex;gap:14px}
.organizer .badge{font-size:11px;background:var(--navy);color:#fff;padding:2px 8px;height:20px}
.brand{display:flex;align-items:center;gap:8px;font-family:"Shippori Mincho",serif;font-weight:800;font-size:24px;color:var(--navy)}
.brand i{width:16px;height:16px;border-radius:50%;background:var(--orange);display:block}
.org-info{margin-top:8px;font-size:11px;line-height:1.65;color:var(--ink)}
.org-info .name{font-weight:700;font-size:12px}
</style>
</head>
<body>
<div class="flyer">

  <div class="date-tag">
    <div class="kind">オンライン講座</div>
    <div class="year">2021</div>
    <div class="day">9/24<small>(金)</small></div>
    <div class="time">19:00〜20:00</div>
    <div class="note">定員 先着10名様</div>
  </div>

  <h1 class="headline">
    <span class="l1">言葉が人を<em>動かす</em>、</span>
    <span class="l2"><em>自分</em>を変える</span>
  </h1>

  <svg class="mug" role="img" aria-label="ロゴ入りのコーヒーマグのイラスト" viewBox="0 0 194 206">
    <defs><linearGradient id="mugTone" x1="0" x2="1"><stop offset="0" stop-color="#2a3f5e"/><stop offset="1" stop-color="#1b2c45"/></linearGradient></defs>
    <rect x="0" y="0" width="194" height="206" rx="14" fill="url(#mugTone)"/>
  </svg>

  <div class="theme-card">
    <svg class="cube" role="img" aria-label="段ボール箱のイラスト" viewBox="0 0 58 56"><rect width="58" height="56" fill="#d9b98a"/></svg>
    <h2 class="theme-title">ローレンス元大統領の<br>スピーチに隠された<br><span class="accent">伝える力</span>とは？</h2>
    <svg class="pencil" role="img" aria-label="鉛筆のイラスト" viewBox="0 0 70 14"><rect width="70" height="14" fill="#e5843a"/></svg>
  </div>

  <div class="home-study">自宅で学べる</div>
  <table class="details">
    <tr><th>日時</th><td>9月24日(金)<br>19:00〜20:00</td></tr>
    <tr><th>講師</th><td>みなと話し方講師</td></tr>
    <tr><th>定員</th><td>10名（先着順）</td></tr>
  </table>

  <div class="question">どうして人前で<br>あがってしまうのか？</div>
  <div class="curriculum">
    <div class="label"><span>カリキュラム</span>オンライン 60分講座</div>
    <ul>
      <li>講師の告白！あがり症で悩んだ日々</li>
      <li>あがり症があらわれる原因とは</li>
      <li>緊張は一瞬で解ける？簡単ワーク</li>
      <li>あがり症改善のための実践トレーニング</li>
      <li>緊張を上手にコントロールする方法</li>
    </ul>
  </div>

  <div class="stories">
    <section class="story s-left">
      <h3>伝わる話し方は<em>誰でも</em>身につけられる</h3>
      <p>名スピーチと呼ばれる演説には、聞く人の心を動かす共通の型があります。</p>
      <p>言葉の選び方、間の取り方、視線の置き方。どれも特別な才能ではありません。</p>
      <p>本講座では<span class="hl">身近な場面で使える技術</span>として、会議や面接、</p>
      <p>プレゼンテーションにすぐ活かせる形でお伝えします。</p>
      <p>話すことへの苦手意識を、自信へと変える一時間にしませんか。</p>
    </section>
    <section class="story s-mid">
      <h3>授業中の発表で<em>全然話せなかった</em>日々</h3>
      <p>学生の頃、人前に立つと頭が真っ白になり、</p>
      <p>用意した言葉がひとつも出てきませんでした。</p>
      <p>社会人になっても会議での発言が怖く、</p>
      <p>そんな自分を変えたいと学び始めたのが話し方でした。</p>
      <p>今では<span class="hl">多くの方の前で講演</span>をしています。</p>
    </section>
    <section class="story s-right">
      <h3>日本人は<em>ユーモア</em>を使えない？</h3>
      <p>あいさつ、自己紹介、プレゼンテーション。</p>
      <p>場を和ませるひと言があるだけで、</p>
      <p>相手との距離はぐっと縮まります。</p>
      <p><span class="hl">緊張をほぐす言葉の力</span>を一緒に学びましょう。</p>
    </section>
  </div>

  <footer class="footer">
    <div class="contact">
      <span class="cap">受講申込・問合せ</span>
      <div class="tel">
        <svg viewBox="0 0 36 24" aria-hidden="true"><rect x="0" y="2" width="36" height="20" rx="10" fill="none" stroke="#1f3350" stroke-width="2.5"/><path d="M12 8c0 5 5 9 10 9l2-3-3-2-2 1c-2-1-3-2-4-4l1-2-2-3z" fill="#1f3350"/></svg>
        0120-394-667
      </div>
      <div class="hours">電話受付：平日９時〜17時</div>
    </div>

    <div class="search">
      <span class="word">そらのわ</span>
      <span class="btn"><svg width="12" height="12" viewBox="0 0 12 12" aria-hidden="true"><circle cx="5" cy="5" r="3.5" fill="none" stroke="#fff" stroke-width="1.6"/><path d="M7.6 7.6 11 11" stroke="#fff" stroke-width="1.6"/></svg></span>
    </div>

    <div class="organizer">
      <span class="badge">主催</span>
      <div>
        <div class="brand"><i></i>そらのわ</div>
        <div class="org-info">
          <div class="name">一般社団法人あおぞら地域交流センター</div>
          <div>〒521-0342滋賀県米原市柏原台4-7-15</div>
          <div>TEL.0749-38-2951</div>
        </div>
      </div>
    </div>
  </footer>

</div>
</body>
</html>
```